Zielgruppe
Elektro und Automatisierungstechnik
Zielgruppe: Industriekunden
Aufgabenstellung
Zweiseitig farbig
Querformat 8,5*5,5cm
modernes, innovatives und zuverlässiges Unternehmen
Vorhandenes Logo muss integriert werden. Siehe Anhang

```html
<!DOCTYPE html>
<html lang="de">
<head>
<meta charset="utf-8">
<title>Kolsin Elektrotechnik – Visitenkarte</title>
<link rel="stylesheet" href="https://fonts.googleapis.com/css2?family=Montserrat:wght@400;700&display=swap">
<style>
  :root {
    --page-bg: #b8b8b8;
    --card-white: #ffffff;
    --navy: #173756;
    --navy-light: #2a4a6e;
    --navy-shade: #0c1c2c;
    --strip-grey: #646464;
    --band-top: #363636;
    --band-bottom: #1c1c1c;
    --text-dark: #2b2b2b;
  }
  html, body {
    margin: 0;
    width: 1200px;
    height: 1200px;
    overflow: hidden;
    background: var(--page-bg);
    font-family: "Montserrat", sans-serif;
  }
  .card {
    position: absolute;
    left: 252px;
    width: 695px;
    height: 397px;
    display: block;
  }
  .card--front { top: 163px; }
  .card--back { top: 620px; }
  .card-base { fill: var(--card-white); }
  .edge-grey { fill: var(--strip-grey); }
  .edge-navy { fill: var(--navy); }
  .edge-navy-light { fill: var(--navy-light); }
  .brand-mark { fill: var(--navy); }
  .brand-name, .brand-trade {
    fill: var(--navy);
    font-family: "Montserrat", sans-serif;
    font-weight: 700;
  }
  .ribbon { fill: var(--navy); }
  .ribbon-fold { fill: var(--navy-shade); }
  .holder-name {
    fill: #ffffff;
    font-family: "Montserrat", sans-serif;
    font-weight: 700;
    font-size: 37px;
    letter-spacing: 1px;
  }
  .holder-role {
    fill: #ffffff;
    font-family: "Montserrat", sans-serif;
    font-weight: 400;
    font-size: 22px;
    letter-spacing: 0.5px;
  }
  .contact-text {
    fill: var(--text-dark);
    font-family: "Montserrat", sans-serif;
    font-weight: 400;
    font-size: 15px;
    letter-spacing: 0.3px;
  }
  .contact-tab { fill: var(--navy); }
  .contact-fold { fill: var(--navy-shade); }
  .contact-icon { fill: #ffffff; }
  .contact-icon-line { fill: none; stroke: #ffffff; stroke-width: 1.2; }
</style>
</head>
<body>

<!-- Front side -->
<svg class="card card--front" viewBox="0 0 695 397" aria-label="Kolsin Elektrotechnik, Vorderseite">
  <defs></defs>
  <rect class="card-base" x="0" y="0" width="695" height="397"/>
  <rect class="edge-grey" x="0" y="0" width="28" height="194"/>
  <rect class="edge-navy-light" x="0" y="194" width="28" height="10"/>
  <rect class="edge-navy" x="0" y="204" width="28" height="188"/>

  <g class="brand">
    <rect class="brand-mark" x="145" y="212" width="28" height="28"/>
    <text class="brand-name" x="187" y="240" font-size="66" textLength="364" lengthAdjust="spacingAndGlyphs">KOLSIN</text>
    <text class="brand-trade" x="187" y="277" font-size="28" textLength="364" lengthAdjust="spacingAndGlyphs">ELEKTROTECHNIK</text>
  </g>
</svg>

<!-- Back side -->
<svg class="card card--back" viewBox="0 0 695 397" aria-label="Kolsin Elektrotechnik, Rückseite mit Kontaktdaten">
  <defs>
    <linearGradient id="band-shade" x1="0" y1="0" x2="0" y2="1">
      <stop offset="0" stop-color="var(--band-top)"/>
      <stop offset="1" stop-color="var(--band-bottom)"/>
    </linearGradient>
  </defs>
  <rect class="card-base" x="0" y="0" width="695" height="397"/>
  <rect x="0" y="0" width="695" height="138" fill="url(#band-shade)"/>

  <g class="name-ribbon">
    <polygon class="ribbon-fold" points="123,138 149,95 172,138"/>
    <polygon class="ribbon-fold" points="548,95 573,138 523,138"/>
    <polygon class="ribbon" points="149,95 548,95 499,181 197,181"/>
    <text class="holder-name" x="348" y="137" text-anchor="middle">YOR NAME</text>
    <text class="holder-role" x="348" y="166" text-anchor="middle">POSITION</text>
  </g>

  <rect class="edge-grey" x="651" y="202" width="44" height="195"/>

  <g class="brand">
    <rect class="brand-mark" x="71" y="309" width="18" height="18"/>
    <text class="brand-name" x="99" y="327" font-size="42" textLength="238" lengthAdjust="spacingAndGlyphs">KOLSIN</text>
    <text class="brand-trade" x="99" y="351" font-size="18" textLength="238" lengthAdjust="spacingAndGlyphs">ELEKTROTECHNIK</text>
  </g>

  <g class="contact-list">
    <!-- address -->
    <text class="contact-text" x="616" y="250" text-anchor="end">Your Street Addres Rome, 3333</text>
    <polygon class="contact-fold" points="625,262 651,262 651,274"/>
    <rect class="contact-tab" x="625" y="240" width="70" height="22" rx="3"/>
    <path class="contact-icon" d="M630,252 l7,-6 7,6 h-2 v6 h-3 v-4 h-4 v4 h-3 v-6 z"/>

    <!-- email -->
    <text class="contact-text" x="616" y="284" text-anchor="end">yourname@postfach.de</text>
    <polygon class="contact-fold" points="625,296 651,296 651,308"/>
    <rect class="contact-tab" x="625" y="274" width="70" height="22" rx="3"/>
    <path class="contact-icon" d="M630,286 l14,-6 -3,13 -4,-4 -2,3 v-4 l5,-5 -6,4 z"/>

    <!-- web -->
    <text class="contact-text" x="616" y="318" text-anchor="end">www.yourweb.com</text>
    <polygon class="contact-fold" points="625,331 651,331 651,343"/>
    <rect class="contact-tab" x="625" y="309" width="70" height="22" rx="3"/>
    <circle class="contact-icon-line" cx="637" cy="320" r="6"/>
    <ellipse class="contact-icon-line" cx="637" cy="320" rx="2.5" ry="6"/>
    <line class="contact-icon-line" x1="631" y1="320" x2="643" y2="320"/>

    <!-- phone -->
    <text class="contact-text" x="616" y="353" text-anchor="end">+123456789011</text>
    <polygon class="contact-fold" points="625,365 651,365 651,377"/>
    <rect class="contact-tab" x="625" y="343" width="70" height="22" rx="3"/>
    <path class="contact-icon" d="M630,351 q7,-5 14,0 v2 h-3 v-2 h-8 v2 h-3 z M632,354 h10 l1,6 h-12 z"/>
    <circle cx="637" cy="357" r="1.6" fill="var(--navy)"/>
  </g>
</svg>

</body>
</html>
```